Wine label refresh

We are wanting to modify our Corran Hollow label to include a picture on it.
I have attached the pictures below which we would like on the label. They are of the Corran Hollow vineyard. I have also attached an example of another label with a picture on it that we like the style of.
Updates
Industry/Entity Type
Vineyard
Requirements
Must have
- The Corran Hollow text must stay the same but can be moved down. It still needs to be the same size though.
Marlborough Sauvignon Blanc should remain in the same font and roughly the same size.
Wine of New Zealand also must stay but could potentially be moved.
Nice to have
- It would be nice if we could keep the PM logo on the front label but feel free to experiment with where this goes.

```html
<!DOCTYPE html>
<html lang="en">
<head>
<meta charset="utf-8">
<title>Corran Hollow — Marlborough Sauvignon Blanc 2012</title>
<link rel="stylesheet" href="https://fonts.googleapis.com/css2?family=Cormorant+SC:wght@500&family=Cormorant+Garamond:wght@400;500&family=Sorts+Mill+Goudy&family=Lato:wght@300&display=swap">
<style>
  :root {
    --band: #98a0b2;
    --paper: #ffffff;
    --rule: #98a0b2;
    --ink: #111111;
    --varietal: #6a6665;
    --vintage: #b19b97;
    --monogram: #c9b6b2;
    --detail: #5f5c5b;
  }
  html, body {
    margin: 0;
    padding: 0;
    width: 1200px;
    height: 898px;
    overflow: hidden;
    background: var(--band);
  }
  .label {
    position: relative;
    width: 1200px;
    height: 898px;
    background: var(--band);
  }
  .label__paper {
    position: absolute;
    left: 20px; top: 20px; right: 20px; bottom: 20px;
    background: var(--paper);
  }
  .label__rule {
    position: absolute;
    left: 24px; top: 24px; right: 24px; bottom: 24px;
    border: 2px solid var(--rule);
  }
  .monogram {
    position: absolute;
    left: 0; right: 0; top: 40px;
    text-align: center;
    font-family: "Cormorant Garamond", serif;
    font-weight: 400;
    font-size: 190px;
    line-height: 1;
    color: var(--monogram);
    letter-spacing: -18px;
  }
  .estate-name {
    position: absolute;
    left: 0; right: 0; top: 62px;
    margin: 0;
    text-align: center;
    font-family: "Cormorant SC", serif;
    font-weight: 500;
    font-size: 84px;
    line-height: 1;
    color: var(--ink);
    letter-spacing: 4px;
  }
  .estate-name .initial { font-size: 114px; }
  .vineyard-frame {
    position: absolute;
    left: 228px; top: 229px;
    width: 745px; height: 385px;
    border: 2px solid var(--rule);
    box-sizing: border-box;
  }
  .vineyard-photo {
    position: absolute;
    left: 246px; top: 244px;
    width: 711px; height: 354px;
    background: linear-gradient(180deg, #d9dde1 0%, #c7ccd0 30%, #7f8f5c 45%, #4f6d33 62%, #5c8a34 80%, #7a6f4e 100%);
  }
  .varietal {
    position: absolute;
    left: 0; right: 0; top: 628px;
    margin: 0;
    text-align: center;
    font-family: "Sorts Mill Goudy", serif;
    font-weight: 400;
    font-size: 86px;
    line-height: 1;
    color: var(--varietal);
    letter-spacing: -0.5px;
    white-space: nowrap;
  }
  .vintage {
    position: absolute;
    left: 0; right: 0; top: 718px;
    text-align: center;
    font-family: "Cormorant Garamond", serif;
    font-weight: 500;
    font-size: 108px;
    font-variant-numeric: lining-nums;
    font-feature-settings: "lnum" 1;
    line-height: 1;
    color: var(--vintage);
  }
  .details {
    position: absolute;
    left: 62px; right: 62px; top: 824px;
    display: flex;
    justify-content: space-between;
    font-family: "Lato", sans-serif;
    font-weight: 300;
    font-size: 34px;
    line-height: 1;
    color: var(--detail);
  }
</style>
</head>
<body>
  <main class="label">
    <div class="label__paper"></div>
    <div class="label__rule"></div>

    <div class="monogram" aria-hidden="true">PM</div>
    <h1 class="estate-name"><span class="initial">C</span>ORRAN <span class="initial">H</span>OLLOW</h1>

    <div class="vineyard-frame"></div>
    <div class="vineyard-photo" role="img" aria-label="Photograph of the Corran Hollow vineyard: rows of vines leading to a cottage framed by palm trees, green hills under a cloudy sky"></div>

    <h2 class="varietal">Marlborough Sauvignon Blanc</h2>
    <div class="vintage">2012</div>

    <div class="details">
      <span class="volume">750ml</span>
      <span class="origin">NEW ZEALAND WINE</span>
      <span class="abv">13% alc/vol</span>
    </div>
  </main>
</body>
</html>
```